Page for Games Online, Tier842Plays, MMORPG Online,Web Browser

Looking for a good nice page, online games web browser, you may be based a little on what I'm looking for as this sample site: http://958.example

REF: http://www.playzone764.example/
==============================================================
Procuro uma pagina bem agradavel, para jogos online de navegador de internet, vocĂȘ poderao se basear um pouco no que eu estou procurando como esse site de exemplo : http://958.example

Target Market(s)

Page for Games Online, Tier842Plays, MMORPG Online

Industry/Entity Type

Games

Coding

Coded - Design and coding required

Number of Pages Required

2 page

Font styles to use
Serif
Sans Serif

Requirements

```html
<!DOCTYPE html>
<html lang="en">
<head>
<meta charset="utf-8">
<title>Tier842Plays</title>
<link rel="stylesheet" href="https://fonts.googleapis.com/css2?family=Audiowide&family=Arimo:wght@400;700&display=swap">
<style>
:root{
  --ink:#1b2a55;
  --text:#333;
  --muted:#555;
  --line:#e3e3e3;
  --card:#f3f3f3;
  --footer:#262626;
  --star:#f5a623;
  --band-blue:#e6f0f5;
  --band-grey:#efefef;
}
*{box-sizing:border-box;margin:0;padding:0}
html,body{width:677px;height:1200px;overflow:hidden}
body{font-family:"Arimo",Arial,sans-serif;color:var(--text);background:#fff;position:relative}
.site-header{height:58px;border-top:2px solid #1c2333;display:flex;align-items:center;padding:0 56px;position:relative}
.brand{font-family:"Audiowide",sans-serif;font-size:13px;color:var(--ink);letter-spacing:.5px}
.account{position:absolute;right:56px;top:16px;display:flex;gap:6px;align-items:center}
.account .btn{font-size:7px;letter-spacing:.3px;text-transform:uppercase;border:1px solid #ccc;background:#f4f4f4;color:#333;height:19px;padding:0 7px;display:flex;align-items:center;gap:4px}
.menu-icon{margin-left:10px}
.hero{height:250px;position:relative;background:linear-gradient(180deg,#1c2b45 0%,#3a4a5d 45%,#2c3d5a 75%,#1d2f55 100%);display:flex;align-items:center;justify-content:center}
.hero h1{font-family:"Audiowide",sans-serif;color:#fff;font-size:23px;line-height:29px;text-align:center;font-weight:400;letter-spacing:1px;text-transform:uppercase}
.hero .arrow{position:absolute;top:109px;width:17px;height:32px;background:#fff;display:flex;align-items:center;justify-content:center}
.hero .prev{left:0}.hero .next{right:0}
.section{position:relative;padding:0 56px}
.section-head{display:flex;justify-content:space-between;align-items:center;height:20px}
.section-head h2{font-family:"Audiowide",sans-serif;font-size:12px;color:#222;font-weight:400;text-transform:uppercase;letter-spacing:.5px}
.pager{display:flex;gap:4px;font-size:9px;color:#999}
.pager.boxed span{width:10px;height:10px;background:#666;color:#fff;display:flex;align-items:center;justify-content:center;font-size:8px}
.row{display:flex;gap:6px;margin-top:7px}
.card{width:108px;background:var(--card);border:1px solid var(--line);padding:2px;box-shadow:0 1px 2px rgba(0,0,0,.12)}
.thumb{display:block;width:100%}
.card .title{font-size:7px;color:var(--muted);margin:8px 2px 4px}
.tag{display:inline-block;font-size:6px;border:1px solid #ccc;background:#fff;padding:2px 7px;margin-left:2px;color:#555}
.stars{margin-left:2px;display:flex;gap:1px}
.tile{width:108px;height:87px;border:1px solid var(--line);padding:2px;background:#fff;box-shadow:0 1px 2px rgba(0,0,0,.1)}
.tile .thumb{height:100%}
.band{position:absolute;left:0;width:677px}
.band-blue{top:650px;height:196px;background:linear-gradient(180deg,var(--band-blue),#e8f1df)}
.band-grey{top:1002px;height:158px;background:var(--band-grey)}
.video{position:relative;display:flex;flex-direction:column;align-items:center;justify-content:center}
.video .label{position:absolute;top:43px;width:100%;text-align:center;font-size:7px;color:#fff}
.video .stars{position:absolute;top:54px;left:0;right:0;justify-content:center}
.site-footer{position:absolute;left:0;top:1160px;width:677px;height:40px;background:var(--footer);display:flex;align-items:center;padding:0 56px;justify-content:space-between}
.site-footer p{font-size:6.5px;color:#ddd}
.social{display:flex;gap:8px;margin-right:-6px}
.social span{width:19px;height:19px;border:1px solid #ddd;border-radius:50%}
</style>
</head>
<body>
<svg width="0" height="0" style="position:absolute">
  <defs>
    <symbol id="star" viewBox="0 0 10 10"><path d="M5 .5l1.3 2.9 3.2.3-2.4 2.1.7 3.1L5 7.3 2.2 8.9l.7-3.1L.5 3.7l3.2-.3z" fill="#f5a623"/></symbol>
    <symbol id="play" viewBox="0 0 30 30"><circle cx="15" cy="15" r="13" fill="none" stroke="#fff" stroke-width="2"/><path d="M12 9.5l9 5.5-9 5.5z" fill="#fff"/></symbol>
  </defs>
</svg>

<header class="site-header">
  <div class="brand">Tier842Plays</div>
  <nav class="account">
    <span class="btn"><svg width="6" height="7" viewBox="0 0 6 7"><circle cx="3" cy="2" r="1.6" fill="#333"/><path d="M0 7c0-2 1.3-3 3-3s3 1 3 3z" fill="#333"/></svg>Register</span>
    <span class="btn"><svg width="6" height="7" viewBox="0 0 6 7"><rect x="0" y="3" width="6" height="4" fill="#333"/><path d="M1.5 3V2a1.5 1.5 0 0 1 3 0" fill="none" stroke="#333"/></svg>Login</span>
    <svg class="menu-icon" width="16" height="13" viewBox="0 0 16 13"><g fill="#333"><rect width="3" height="3"/><rect x="4" width="12" height="3"/><rect y="5" width="3" height="3"/><rect x="4" y="5" width="12" height="3"/><rect y="10" width="3" height="3"/><rect x="4" y="10" width="12" height="3"/></g></svg>
  </nav>
</header>

<section class="hero" role="img" aria-label="Futuristic city of towers and spaceships under a dark blue sky">
  <span class="arrow prev"><svg width="7" height="11" viewBox="0 0 7 11"><path d="M6 1L1.5 5.5 6 10" fill="none" stroke="#222" stroke-width="2"/></svg></span>
  <h1>Welcome to<br>Tier842Plays</h1>
  <span class="arrow next"><svg width="7" height="11" viewBox="0 0 7 11"><path d="M1 1l4.5 4.5L1 10" fill="none" stroke="#222" stroke-width="2"/></svg></span>
</section>

<section class="section featured" style="margin-top:23px">
  <div class="section-head"><h2>Featured</h2><div class="pager"><span>‹</span><span>›</span></div></div>
  <div class="row" style="margin-top:8px">
    <div class="card"><div class="thumb" style="height:92px;background:linear-gradient(160deg,#1a2b4a,#4f6d8a 60%,#223)" role="img" aria-label="Alien pyramid landscape at night"></div><p class="title">Neque porro quisquam</p><span class="tag">Playing</span></div>
    <div class="card"><div class="thumb" style="height:92px;background:linear-gradient(180deg,#7ea6cf,#c8cfd6 55%,#6c6a62)" role="img" aria-label="Robot walking over a city"></div><p class="title">Neque porro quisquam</p><span class="tag">Playing</span></div>
    <div class="card"><div class="thumb" style="height:92px;background:linear-gradient(180deg,#5aa8e8,#9ccff0 45%,#4aa83c 70%,#2e7d24)" role="img" aria-label="Knight on horseback before a castle"></div><p class="title">Neque porro quisquam</p><span class="tag">Playing</span></div>
    <div class="card"><div class="thumb" style="height:92px;background:linear-gradient(160deg,#7c9bb0,#3c5466 55%,#1e2a33)" role="img" aria-label="Armoured rider in a sci-fi city"></div><p class="title">Neque porro quisquam</p><span class="tag">Playing</span></div>
    <div class="card"><div class="thumb" style="height:92px;background:linear-gradient(180deg,#2a3342,#c98a3e 50%,#3a2f24)" role="img" aria-label="Ships over a city at sunset"></div><p class="title">Neque porro quisquam</p><span class="tag">Playing</span></div>
  </div>
</section>

<section class="section flash" style="margin-top:19px">
  <div class="section-head"><h2>Flash Games</h2><div class="pager"><span>‹</span><span>›</span></div></div>
  <div class="row">
    <div class="tile"><div class="thumb" style="background:linear-gradient(135deg,#d22b10,#f06a2a 50%,#9e1d0a)" role="img" aria-label="Robot figure on a red background"></div></div>
    <div class="tile"><div class="thumb" style="background:linear-gradient(135deg,#3a4fb0,#1a2a70 60%,#0c1440)" role="img" aria-label="Spaceship flying in blue space"></div></div>
    <div class="tile"><div class="thumb" style="background:linear-gradient(180deg,#0f1420,#3b4a5e 60%,#6f8fb8)" role="img" aria-label="Space station above a planet"></div></div>
    <div class="tile"><div class="thumb" style="background:linear-gradient(135deg,#3a0a06,#c2331a 50%,#4a0d08)" role="img" aria-label="Fiery warrior illustration"></div></div>
    <div class="tile"><div class="thumb" style="background:linear-gradient(180deg,#cfd8de,#6f8a98 55%,#2a3b46)" role="img" aria-label="Floating island city"></div></div>
  </div>
</section>

<div class="band band-blue"></div>
<section class="section mmorpg" style="margin-top:27px">
  <div class="section-head"><h2>MMORPG Games</h2><div class="pager boxed"><span>‹</span><span>›</span></div></div>
  <div class="row">
    <div class="card"><div class="thumb" style="height:93px;background:linear-gradient(180deg,#6d6a6a,#3b2c2a 60%,#1a1414)" role="img" aria-label="Gamer before an alien city"></div><p class="title">Neque porro quisquam</p><div class="stars"><svg width="7" height="7"><use href="#star"/></svg><svg width="7" height="7"><use href="#star"/></svg><svg width="7" height="7"><use href="#star"/></svg><svg width="7" height="7"><use href="#star"/></svg><svg width="7" height="7"><use href="#star"/></svg></div></div>
    <div class="card"><div class="thumb" style="height:93px;background:linear-gradient(160deg,#d8dde2,#8e9aa4 55%,#2a2f36)" role="img" aria-label="Child playing at a computer with jets"></div><p class="title">Neque porro quisquam</p><div class="stars"><svg width="7" height="7"><use href="#star"/></svg><svg width="7" height="7"><use href="#star"/></svg><svg width="7" height="7"><use href="#star"/></svg><svg width="7" height="7"><use href="#star"/></svg><svg width="7" height="7"><use href="#star"/></svg></div></div>
    <div class="card"><div class="thumb" style="height:93px;background:linear-gradient(160deg,#3b7ec8,#d8dce2 45%,#b8261f 75%,#1c3e7a)" role="img" aria-label="Casino chips and dice on a keyboard"></div><p class="title">Neque porro quisquam</p><div class="stars"><svg width="7" height="7"><use href="#star"/></svg><svg width="7" height="7"><use href="#star"/></svg><svg width="7" height="7"><use href="#star"/></svg><svg width="7" height="7"><use href="#star"/></svg><svg width="7" height="7"><use href="#star"/></svg></div></div>
    <div class="card"><div class="thumb" style="height:93px;background:radial-gradient(circle at 50% 50%,#2e6e7a,#0e2328 70%)" role="img" aria-label="Sci-fi fighter with red laser beams"></div><p class="title">Neque porro quisquam</p><div class="stars"><svg width="7" height="7"><use href="#star"/></svg><svg width="7" height="7"><use href="#star"/></svg><svg width="7" height="7"><use href="#star"/></svg><svg width="7" height="7"><use href="#star"/></svg><svg width="7" height="7"><use href="#star"/></svg></div></div>
    <div class="card"><div class="thumb" style="height:93px;background:radial-gradient(circle at 50% 40%,#b89be8,#5a2fa8 55%,#1e0f4a)" role="img" aria-label="Playing cards held by gloved hands"></div><p class="title">Neque porro quisquam</p><div class="stars"><svg width="7" height="7"><use href="#star"/></svg><svg width="7" height="7"><use href="#star"/></svg><svg width="7" height="7"><use href="#star"/></svg><svg width="7" height="7"><use href="#star"/></svg><svg width="7" height="7"><use href="#star"/></svg></div></div>
  </div>
</section>

<section class="section online" style="margin-top:36px">
  <div class="section-head"><h2>Online Games</h2><div class="pager"><span>‹</span><span>›</span></div></div>
  <div class="row">
    <div class="tile"><div class="thumb" style="background:linear-gradient(160deg,#2f4a4a,#8a7a55 60%,#3a2f1c)" role="img" aria-label="Chess pieces on a board"></div></div>
    <div class="tile"><div class="thumb" style="background:linear-gradient(180deg,#6aa8d8,#9cc6e2 55%,#3b6d3a)" role="img" aria-label="Floating islands platform scene"></div></div>
    <div class="tile"><div class="thumb" style="background:linear-gradient(180deg,#6ec0ec,#b9dff2 50%,#c98a35)" role="img" aria-label="Arcade fighting game screen"></div></div>
    <div class="tile"><div class="thumb" style="background:linear-gradient(160deg,#2d4a1f,#6e8a2e 50%,#2a3a14)" role="img" aria-label="Mushroom forest landscape"></div></div>
    <div class="tile"><div class="thumb" style="background:linear-gradient(180deg,#8a7ad0,#c8b4e0 40%,#3f8a4a 75%,#2a5a8a)" role="img" aria-label="Colourful floating island with a mountain"></div></div>
  </div>
</section>

<div class="band band-grey"></div>
<section class="section recommended" style="margin-top:32px">
  <div class="section-head"><h2>Recommended Game</h2><div class="pager boxed"><span>‹</span><span>›</span></div></div>
  <div class="row" style="margin-top:6px">
    <div class="tile video"><div class="thumb" style="background:linear-gradient(160deg,#3a3a3a,#1a1a1a)" role="img" aria-label="Armoured soldier in shadow"></div><svg width="22" height="22" style="position:absolute;top:15px"><use href="#play"/></svg><span class="label">Neque porro quisquam</span><div class="stars"><svg width="7" height="7"><use href="#star"/></svg><svg width="7" height="7"><use href="#star"/></svg><svg width="7" height="7"><use href="#star"/></svg><svg width="7" height="7"><use href="#star"/></svg><svg width="7" height="7"><use href="#star"/></svg></div></div>
    <div class="tile video"><div class="thumb" style="background:linear-gradient(160deg,#1a2238,#6b6560 60%,#8a5a3a)" role="img" aria-label="Astronaut on a rocky planet"></div><svg width="30" height="30" style="position:absolute"><use href="#play"/></svg></div>
    <div class="tile video"><div class="thumb" style="background:linear-gradient(180deg,#5b7fb0,#8a9bb0 50%,#a0805a)" role="img" aria-label="Walking robot in a desert"></div><svg width="30" height="30" style="position:absolute"><use href="#play"/></svg></div>
    <div class="tile video"><div class="thumb" style="background:linear-gradient(180deg,#8a7a68,#6a5a48 60%,#3a2e22)" role="img" aria-label="Archer among stone ruins"></div><svg width="30" height="30" style="position:absolute"><use href="#play"/></svg></div>
    <div class="tile video"><div class="thumb" style="background:linear-gradient(160deg,#5a5a5a,#2a2a2a)" role="img" aria-label="Armoured figure in a corridor"></div><svg width="30" height="30" style="position:absolute"><use href="#play"/></svg></div>
  </div>
</section>

<footer class="site-footer">
  <p>© Copy Rights 2015 Tier842Plays.All Rights Reserved.</p>
  <div class="social"><span></span><span></span><span></span><span></span></div>
</footer>
</body>
</html>
```